Equine Website flyer design

www.brightpaddock.co.uk

Fresh Stable & Spare Tack Supplies

I need a flyer to advertise my website selling all you need for horse & rider apart from hats & saddles. It only needs to be one sided.

My business colours are pink & blue, please take a look at my website to give you ideas of how I run.

I am unsure as to weather to add pictures of examples of products from the website?

It needs to say that I stock everything for horse & rider apart from hats & saddles, second hand & new. All at very good prices

Why buy new when you can buy second hand?

Industry/Entity Type

Business

Requirements
Should not have
• My address, I am a website NOT a shop!

```html
<!DOCTYPE html>
<html lang="en">
<head>
<meta charset="utf-8">
<title>Bright Paddock flyer</title>
<link rel="stylesheet" href="https://fonts.googleapis.com/css2?family=Didact+Gothic&family=PT+Sans+Narrow:wght@400;700&family=Nunito:wght@900&family=Anton&family=Arimo:ital,wght@1,700&display=swap">
<style>
:root{
  --sky:#55c4ee;
  --blush:#edbde8;
  --magenta:#ee2fd2;
  --ink:#1c1c1c;
  --night:#111111;
  --ice:#8fe3ff;
  --white:#ffffff;
  --device:#3a3d44;
}
*{margin:0;padding:0;box-sizing:border-box}
html,body{width:851px;height:1200px;overflow:hidden;background:var(--sky)}
.flyer{position:relative;width:851px;height:1200px;background:var(--sky);font-family:"PT Sans Narrow",sans-serif;color:var(--ink)}
.panel{position:absolute;background:var(--blush)}
.panel--intro{left:22px;top:22px;width:808px;height:403px}
.panel--visit{left:22px;top:460px;width:808px;height:326px}
.panel--about{left:22px;top:997px;width:808px;height:173px}
.masthead{position:absolute;left:8px;top:11px;width:792px;height:75px;background:var(--night);text-align:center}
.masthead__name{font-family:"Didact Gothic",sans-serif;color:var(--magenta);font-size:38px;line-height:40px;padding-top:4px;letter-spacing:1px}
.masthead__tagline{font-family:"Didact Gothic",sans-serif;color:var(--ice);font-size:24px;line-height:26px;letter-spacing:.5px}
.headline{position:absolute;left:18px;top:122px;font-family:"Didact Gothic",sans-serif;color:var(--magenta);font-size:50px;line-height:58px}
.headline span{display:block}
.headline span+span{padding-left:44px}
.benefits{position:absolute;left:18px;top:246px;list-style:none;font-size:28px;line-height:33px}
.benefits li{position:relative;padding-left:32px}
.benefits li::before{content:"";position:absolute;left:4px;top:8px;width:17px;height:17px;background:var(--magenta);transform:rotate(45deg)}
.benefits .indent{display:block}
.artwork{position:absolute;left:598px;top:158px;width:210px;height:245px;background:linear-gradient(160deg,#f6dff3,#e5b2df)}
.visit-label{position:absolute;left:0;top:424px;width:851px;text-align:center;color:var(--white);font-weight:700;font-size:32px;line-height:36px}
.site-url{position:absolute;left:0;top:12px;width:808px;text-align:center;font-family:"Nunito",sans-serif;font-weight:900;color:var(--magenta);font-size:52px;line-height:60px}
.device{position:absolute}
.device--tablet{left:21px;top:86px;width:144px;height:216px}
.device--monitor{left:194px;top:86px;width:300px;height:240px}
.offer{position:absolute;left:494px;top:122px;width:300px;text-align:center;font-family:"Arimo",sans-serif;font-style:italic;font-weight:700;font-size:22px;line-height:28px}
.cta{position:absolute;left:494px;top:228px;width:300px;text-align:center;font-family:"Anton",sans-serif;color:var(--magenta);font-size:46px;line-height:56px}
.gallery{position:absolute;left:0;top:786px;width:851px;height:211px}
.gallery__shot{position:absolute;top:0;height:211px}
.about__text{position:absolute;left:16px;top:4px;width:780px;font-size:20px;line-height:23.5px}
.about__text strong{color:var(--magenta);font-weight:700}
.social{position:absolute;top:121px;width:150px;height:47px;border-radius:6px;display:flex;align-items:center;justify-content:center;gap:8px;font-size:20px;line-height:22px}
.social--friendwall{left:223px;background:#e9eef7;color:#2b4a8a}
.social--chirper{left:436px;background:#6fcbea;color:var(--white)}
.social__dot{width:22px;height:22px;border-radius:50%;background:currentColor;flex:none}
</style>
</head>
<body>
<main class="flyer">
  <section class="panel panel--intro">
    <header class="masthead">
      <div class="masthead__name">BRIGHT PADDOCK.co.uk</div>
      <div class="masthead__tagline">FRESH STABLE &amp; SPARE TACK SUPPLIES</div>
    </header>
    <h1 class="headline"><span>Why Buy New When You</span><span>Can Buy Gently Used?</span></h1>
    <ul class="benefits">
      <li>Buy everything you need ONLINE for<span class="indent">horse and rider (apart from hats and saddles).</span></li>
      <li>Second hand and new</li>
      <li>All at very good prices</li>
    </ul>
    <div class="artwork" role="img" aria-label="Line drawing of a rider embracing her horse"></div>
  </section>

  <div class="visit-label">Please Visit</div>

  <section class="panel panel--visit">
    <div class="site-url">www.brightpaddock.co.uk</div>
    <svg class="device device--tablet" viewBox="0 0 144 216" aria-hidden="true">
      <rect x="0" y="0" width="144" height="216" rx="10" fill="var(--device)"/>
    </svg>
    <div class="device" style="left:33px;top:104px;width:120px;height:180px;background:linear-gradient(180deg,#f4f4f4 0%,#9ccf6a 45%,#e8e8e8 80%)" role="img" aria-label="Online shop homepage shown on a tablet"></div>
    <svg class="device device--monitor" viewBox="0 0 300 240" aria-hidden="true">
      <rect x="0" y="0" width="300" height="190" rx="6" fill="var(--device)"/>
      <rect x="0" y="180" width="300" height="12" fill="#2a2c31"/>
      <path d="M125 192 L175 192 L182 230 L118 230 Z" fill="var(--device)"/>
      <rect x="105" y="228" width="90" height="8" rx="3" fill="#2a2c31"/>
    </svg>
    <div class="device" style="left:207px;top:97px;width:274px;height:162px;background:linear-gradient(180deg,#f4f4f4 0%,#cfe6f5 35%,#a98a6a 70%,#eeeeee 100%)" role="img" aria-label="Online shop rider wear page shown on a desktop monitor"></div>
    <p class="offer">Saddlery, tack, apparel,<br>&amp; gifts for riders<br>and horses</p>
    <p class="cta">BUY ONLINE!</p>
  </section>

  <div class="gallery">
    <div class="gallery__shot" style="left:0;width:283px;background:linear-gradient(180deg,#9fc4e6 0%,#2a2a2a 30%,#3c3c3c 65%,#6f9a3c 100%)" role="img" aria-label="Market gazebo stall stocked with rugs and riding wear"></div>
    <div class="gallery__shot" style="left:285px;width:283px;background:linear-gradient(180deg,#2b2b2b 0%,#b8a6d4 45%,#1e1e1e 100%)" role="img" aria-label="Horse rugs and saddle cloths hanging on a rail"></div>
    <div class="gallery__shot" style="left:570px;width:281px;background:linear-gradient(180deg,#c9e3ee 0%,#8fae5a 40%,#5e8a34 100%)" role="img" aria-label="Cob in a spotted rug standing in a green field"></div>
  </div>

  <section class="panel panel--about">
    <p class="about__text">Bright Paddock is run by Jess from her home in Ashcombe. She stocks everything for horse &amp; rider (apart from hats &amp; saddles) second hand &amp; new &amp; some really lovely home things too! Please do take a look at her website <strong>www.brightpaddock.co.uk</strong> There is new things going on everyday! If there is ANYTHING she can help you with, please do ask.</p>
    <div class="social social--friendwall"><span class="social__dot"></span><span>Join us on<br>Friendwall</span></div>
    <div class="social social--chirper"><span class="social__dot"></span><span>follow us on<br>Chirper</span></div>
  </section>
</main>
</body>
</html>
```